BrimstoneHoldingsLLC

Real Estate Investment. Buy/Sell house/investment . Trustworthy,Reliable, and friendly

Industry/Entity Type

Real Estate

Contact Information for Business Card

BrimstoneHoldings@mailtrove.com
555-413-2960
Tamsin-Leigh Okafor

```html
<!DOCTYPE html>
<html lang="en">
<head>
<meta charset="utf-8">
<title>Brimstone Holdings LLC – Business Card</title>
<link rel="stylesheet" href="https://fonts.googleapis.com/css2?family=Roboto+Slab:wght@500;700;800&display=swap">
<style>
  :root {
    --page-bg: #e9e6e1;
    --card-white: #ffffff;
    --brand-green: #00a33a;
    --brand-green-deep: #0a6b2a;
    --ink-green: #0c4a1e;
    --ink-dark: #0f2a16;
    --text-white: #ffffff;
  }
  * { margin: 0; padding: 0; box-sizing: border-box; }
  html, body {
    width: 1200px;
    height: 675px;
    overflow: hidden;
    background: var(--page-bg);
    font-family: "Roboto Slab", Georgia, serif;
  }
  .card {
    position: absolute;
    left: 75px;
    top: 37px;
    width: 1050px;
    height: 600px;
    background: var(--brand-green);
    overflow: hidden;
    box-shadow: 0 6px 18px rgba(0,0,0,0.18);
  }
  .card__swoosh {
    position: absolute;
    inset: 0;
    width: 1050px;
    height: 600px;
  }
  .card__swoosh .white-field { fill: var(--card-white); }
  .card__swoosh .accent-stripe { fill: var(--brand-green-deep); }

  .company-name {
    position: absolute;
    left: 120px;
    top: 52px;
    font-size: 58px;
    font-weight: 800;
    letter-spacing: 1px;
    color: var(--brand-green);
    text-transform: uppercase;
    white-space: nowrap;
  }
  .services {
    position: absolute;
    left: 70px;
    top: 138px;
    list-style: none;
    font-size: 17px;
    font-weight: 700;
    line-height: 25px;
    color: var(--ink-green);
    text-transform: uppercase;
  }
  .services li::before {
    content: "";
    display: inline-block;
    width: 8px;
    height: 8px;
    border-radius: 50%;
    background: var(--ink-dark);
    margin-right: 12px;
    vertical-align: middle;
    position: relative;
    top: -2px;
  }
  .contact {
    position: absolute;
    left: 560px;
    top: 390px;
  }
  .contact__name {
    font-size: 30px;
    font-weight: 800;
    color: var(--text-white);
    text-transform: uppercase;
    letter-spacing: 0.5px;
    white-space: nowrap;
  }
  .contact__email {
    margin-top: 14px;
    font-size: 25px;
    font-weight: 500;
    color: var(--ink-dark);
    white-space: nowrap;
  }
  .contact__phone {
    margin-top: 12px;
    font-size: 30px;
    font-weight: 800;
    color: var(--ink-dark);
    letter-spacing: 1px;
  }
</style>
</head>
<body>
  <div class="card">
    <svg class="card__swoosh" viewBox="0 0 1050 600" aria-hidden="true">
      <path class="accent-stripe" d="M300,345 C560,420 850,400 1050,330 L1050,372 C860,440 560,445 300,345 Z"/>
      <path class="white-field" d="M0,0 H1050 V330 C850,400 560,420 300,345 C190,310 90,285 0,285 Z"/>
    </svg>

    <h1 class="company-name">Brimstone Holdings LLC</h1>

    <ul class="services">
      <li>Real Estate Investment</li>
      <li>Buy/Sell House/Investment</li>
      <li>Trustworthy</li>
      <li>Reliable</li>
      <li>Friendly</li>
    </ul>

    <div class="contact">
      <p class="contact__name">Tamsin-Leigh Okafor</p>
      <p class="contact__email">BrimstoneHoldings@mailtrove.com</p>
      <p class="contact__phone">555-413-2960</p>
    </div>
  </div>
</body>
</html>
```